Business card for a shipping supplies business

Needing a business card design. Please see the logo. The logo with the white font should be used if there is a dark background.

We are looking for the following info on the card. Please see the sample info. We will need the info to be changed with a few different employee names and info but all will use the same template.

Business Name: The Crate Heron
Employee Name : Marcus Delaney
Position: Account Manager
Address: 4827 W. Ridge 418 S.
Fort Worth, TX 73948
email: Marcus@thecrateheron.example
telephone: 855-619-2740 x 207
website: www.getparcelkits.example

Target Market(s)

Businesses who ship products for online sales

Industry/Entity Type

Cardboard

Contact Information for Business Card

Name, title, address, website, logo, telephone number

Font styles to use
Sans Serif

Colors
EE7325
F08F49
F5BC92
FAE3D3
FDF4ED

Requirements
Must have
• Logo on back of card. Clean look, just logo, website address

```html
<!DOCTYPE html>
<html lang="en">
<head>
<meta charset="utf-8">
<title>The Crate Heron – Business Card</title>
<link href="https://fonts.googleapis.com/css2?family=Poppins:wght@400;500;600;700&display=swap" rel="stylesheet">
<style>
  :root {
    --backdrop: #8c8c8c;
    --card-light: #c6c6ca;
    --card-orange: #c4572a;
    --accent-orange: #c9562a;
    --rust: #7e2f1a;
    --deep-red: #7a2a1c;
    --ink: #141414;
    --icon-grey: #8e8e92;
    --white: #f3f3f3;
  }
  * { box-sizing: border-box; margin: 0; padding: 0; }
  html, body { width: 1200px; height: 1101px; overflow: hidden; }
  body {
    background: var(--backdrop);
    font-family: "Poppins", sans-serif;
    position: relative;
    color: var(--ink);
  }
  .card { position: absolute; width: 302px; height: 530px; }
  .card--front { left: 246px; top: 268px; background: var(--card-light); }
  .card--back  { left: 641px; top: 267px; background: var(--card-orange); }

  .brand-mark { position: absolute; display: flex; align-items: center; gap: 6px; }
  .brand-mark__square { background: var(--deep-red); }
  .brand-mark__name { font-weight: 700; color: var(--accent-orange); text-transform: uppercase; line-height: 1; }

  .front-brand { right: 30px; top: 38px; }
  .front-brand .brand-mark__square { width: 14px; height: 14px; }
  .front-brand .brand-mark__name { font-size: 11px; letter-spacing: 0.5px; }

  .person { position: absolute; left: 33px; top: 176px; }
  .person__first { font-size: 29px; font-weight: 400; color: var(--rust); line-height: 1; letter-spacing: 0.5px; }
  .person__last { font-size: 40px; font-weight: 700; color: var(--accent-orange); line-height: 1; margin-top: 4px; }

  .rule { position: absolute; height: 2px; background: var(--ink); }
  .rule--top { left: 33px; width: 227px; top: 262px; }
  .rule--bottom { left: 33px; width: 227px; top: 413px; }

  .role { position: absolute; left: 33px; top: 276px; font-size: 14.5px; font-weight: 500; letter-spacing: 0.3px; }

  .icons { position: absolute; left: 38px; top: 360px; display: flex; gap: 18px; }
  .icon { width: 32px; height: 32px; border-radius: 3px; display: flex; align-items: center; justify-content: center; }
  .icon--phone { background: var(--accent-orange); }
  .icon--mail { background: var(--icon-grey); }
  .icon--web { background: var(--deep-red); }

  .contact { position: absolute; left: 33px; top: 431px; list-style: none; font-size: 12.5px; font-weight: 500; letter-spacing: 1px; line-height: 21px; text-transform: uppercase; }

  .back-brand { left: 0; right: 0; top: 232px; justify-content: center; gap: 10px; }
  .back-brand .brand-mark__square { width: 26px; height: 26px; }
  .back-brand .brand-mark__name { font-size: 26px; color: var(--ink); }

  .location { position: absolute; left: 33px; right: 32px; top: 412px; display: flex; align-items: center; gap: 12px; }
  .location__line { flex: 1; height: 2px; background: var(--ink); }
  .location__pin { width: 34px; height: 34px; background: var(--deep-red); border-radius: 3px; display: flex; align-items: center; justify-content: center; }
  .address { position: absolute; left: 0; right: 0; top: 464px; text-align: center; font-size: 15.5px; font-weight: 500; line-height: 21px; letter-spacing: 0.3px; }
</style>
</head>
<body>
  <section class="card card--front">
    <div class="brand-mark front-brand">
      <span class="brand-mark__square"></span>
      <span class="brand-mark__name">The Crate Heron</span>
    </div>
    <div class="person">
      <p class="person__first">MARCUS</p>
      <p class="person__last">DELANEY</p>
    </div>
    <div class="rule rule--top"></div>
    <p class="role">ACCOUNT MANAGER</p>
    <div class="icons">
      <span class="icon icon--phone"><svg width="20" height="20" viewBox="0 0 24 24"><path fill="#f3f3f3" d="M6.6 10.8a15.1 15.1 0 0 0 6.6 6.6l2.2-2.2c.3-.3.7-.4 1-.2 1.1.4 2.3.6 3.6.6.6 0 1 .4 1 1V20c0 .6-.4 1-1 1C10.6 21 3 13.4 3 4c0-.6.4-1 1-1h3.5c.6 0 1 .4 1 1 0 1.3.2 2.5.6 3.6.1.3 0 .7-.2 1z"/></svg></span>
      <span class="icon icon--mail"><svg width="22" height="16" viewBox="0 0 22 16"><rect x="1" y="1" width="20" height="14" rx="1" fill="none" stroke="#f3f3f3" stroke-width="1.6"/><path d="M1.5 1.5 11 9l9.5-7.5" fill="none" stroke="#f3f3f3" stroke-width="1.6"/></svg></span>
      <span class="icon icon--web"><svg width="22" height="22" viewBox="0 0 24 24" fill="none" stroke="#f3f3f3" stroke-width="1.5"><circle cx="12" cy="12" r="9.5"/><ellipse cx="12" cy="12" rx="4.5" ry="9.5"/><path d="M2.5 12h19M4 7h16M4 17h16M12 2.5v19"/></svg></span>
    </div>
    <div class="rule rule--bottom"></div>
    <ul class="contact">
      <li>855-619-2740 x 207</li>
      <li>Marcus@thecrateheron.example</li>
      <li>www.getparcelkits.example</li>
    </ul>
  </section>

  <section class="card card--back">
    <div class="brand-mark back-brand">
      <span class="brand-mark__square"></span>
      <span class="brand-mark__name">The Crate Heron</span>
    </div>
    <div class="location">
      <span class="location__line"></span>
      <span class="location__pin"><svg width="18" height="22" viewBox="0 0 18 22"><path fill="#f3f3f3" d="M9 0a8 8 0 0 0-8 8c0 6 8 14 8 14s8-8 8-14a8 8 0 0 0-8-8zm0 11.5A3.5 3.5 0 1 1 9 4.5a3.5 3.5 0 0 1 0 7z"/></svg></span>
      <span class="location__line"></span>
    </div>
    <p class="address">4827 W. Ridge 418 S.<br>Fort Worth, TX 73948</p>
  </section>
</body>
</html>
```